RIVERSTONE PAVING & EARTHWORKS

I would like the front of the card to have my logo centred.
I need it to have my contact details on the back of the card which are: RiverstonePavingEarthworks@mailbrook.net
0439268417
and a Facebook icon

```html
<!DOCTYPE html>
<html lang="en">
<head>
<meta charset="utf-8">
<title>Riverstone Paving &amp; Earthworks – Business Card</title>
<link rel="stylesheet" href="https://fonts.googleapis.com/css2?family=Saira+Condensed:wght@400;700;800&display=swap">
<style>
  :root {
    --backdrop: #5b5b5d;
    --card-black: #151516;
    --brand-blue: #2f6fd6;
    --ink-white: #ffffff;
    --band-black: #111112;
    --concrete-light: #8a8a8a;
    --concrete-mid: #5e5e5e;
    --concrete-dark: #3a3a3a;
    --rule-grey: #8c8c8c;
  }
  * { margin: 0; padding: 0; box-sizing: border-box; }
  html, body {
    width: 1200px;
    height: 900px;
    overflow: hidden;
    background: var(--backdrop);
  }
  .sheet {
    position: relative;
    width: 1200px;
    height: 900px;
    display: flex;
    flex-direction: column;
    align-items: center;
    justify-content: center;
    gap: 60px;
  }
  .card {
    position: relative;
    width: 525px;
    height: 300px;
    border-radius: 4px;
    overflow: hidden;
    box-shadow: 0 10px 28px rgba(0, 0, 0, 0.35);
  }

  /* Front */
  .card-front {
    background: var(--card-black);
    display: flex;
    flex-direction: column;
    align-items: center;
    justify-content: center;
    gap: 16px;
  }
  .brand-mark {
    width: 56px;
    height: 56px;
    background: var(--brand-blue);
  }
  .brand-name {
    font-family: "Saira Condensed", sans-serif;
    font-weight: 800;
    color: var(--brand-blue);
    text-align: center;
    line-height: 1;
    letter-spacing: 0.02em;
    white-space: nowrap;
  }
  .brand-name .line-main { display: block; font-size: 40px; }
  .brand-name .line-sub { display: block; font-size: 28px; margin-top: 4px; }

  /* Back */
  .card-back { background: var(--concrete-mid); }
  .concrete-texture {
    position: absolute;
    inset: 0;
    background:
      radial-gradient(ellipse at 20% 30%, var(--concrete-light) 0%, transparent 55%),
      radial-gradient(ellipse at 80% 75%, var(--concrete-light) 0%, transparent 50%),
      linear-gradient(135deg, var(--concrete-dark), var(--concrete-mid) 50%, var(--concrete-dark));
  }
  .contact-band {
    position: absolute;
    left: 100px;
    top: 80px;
    width: 345px;
    height: 140px;
    background: var(--band-black);
    display: flex;
    flex-direction: column;
    justify-content: center;
    padding: 0 22px;
  }
  .contact-phone {
    font-family: "Saira Condensed", sans-serif;
    font-weight: 700;
    font-size: 56px;
    line-height: 1;
    color: var(--ink-white);
    letter-spacing: 0.01em;
    white-space: nowrap;
  }
  .contact-rule {
    height: 1px;
    background: var(--rule-grey);
    margin: 10px 0 8px;
  }
  .contact-email {
    font-family: "Saira Condensed", sans-serif;
    font-weight: 400;
    font-size: 15px;
    line-height: 1.2;
    color: var(--ink-white);
    white-space: nowrap;
  }
  .social-dot {
    position: absolute;
    right: 28px;
    top: 24px;
    width: 20px;
    height: 20px;
    border-radius: 50%;
    background: var(--ink-white);
  }
</style>
</head>
<body>
  <main class="sheet">
    <section class="card card-front" aria-label="Card front">
      <span class="brand-mark" aria-hidden="true"></span>
      <h1 class="brand-name">
        <span class="line-main">RIVERSTONE PAVING</span>
        <span class="line-sub">&amp; EARTHWORKS</span>
      </h1>
    </section>

    <section class="card card-back" aria-label="Card back">
      <div class="concrete-texture" role="img" aria-label="Weathered grey concrete surface texture"></div>
      <div class="contact-band">
        <p class="contact-phone">043 926 8417</p>
        <div class="contact-rule"></div>
        <p class="contact-email">RiverstonePavingEarthworks@mailbrook.net</p>
      </div>
      <span class="social-dot" aria-label="Social media link"></span>
    </section>
  </main>
</body>
</html>
```